Nutrition Company Needs Labels That Define Brand

Natural health supplement company looking for label designs that can define brand. Bold, Clean, Crisp. Product is Apple Cider Vinegar Gummies. Bottle will be clear, colors suggested are white, red, black, green, gold. All colors don't need to used, just suggestions. Apple images, icons welcomed. Will send examples of working design as requested. In progress design below

Target Market(s)

25-65+ Health Conscious, Energetic and Active lifestyle.

Font styles to use
Sans Serif

Colors
ec1f27
f04a50
f59296
87d0c7
17b099
86cfc6
ffffff
ffc214
ffcf3e

Requirements
Must have
• ⚠ IMPORTANT ⚠
Design in a CMYK format (not RGB).
Upload the label without the “Information” layer (DELETE this layer, including the Bleed & Safe outlines).
All vector text and pathways should be converted to outlines.
Save the file as a PDF
Ensure all product claims have this symbol † after them
DO NOT MODIFY FORMATTING OR FONT SIZES ON THE FACTS PANEL.
SAFE ZONE:
All critical elements (text, images, graphic elements, logos, etc.) must be kept inside the red line. Anything left outside of the red area may be cut off during printing.

BLEED ZONE:
Make sure to extend the background artwork, images or colors to the edge of the blue outline.

SKU / BARCODE:
A unique barcode will be applied to your label in the area marked. Do not apply any color, images or graphics in this area as they will be overwritten. Remove the text "Bar-Code Zone" and leave this area white and clear of any artwork.

QRB PRODUCT CLAIMS:
All product claims (for example, "Lose Weight...") need to have this symbol † after them which references the "These statements have not been evaluated by the QRB..." disclaimer. This is a requirement by the QRB.

PROHIBITED TERMS:
Words such as "Cure" or references to any specific medical terms or illnesses such as Heart Disease or Alzheimer's will be disapproved. Instead use more general terms such as "Supports Your Cardiovascular Health" or "Can Improve Memory Loss".

Products can not be labelled Organic, but they can be called "Natural".

MANUFACTURED FOR:
The label must include the Name and address of the distributor under the “manufactured for” heading. It must also include the Street address if the firm name and address are not listed in a current city directory or telephone book, as well as the City or Town, State, and ZIP code.
Nice to have
• Colors are suggested but not set in stone.
Should not have
• Gimmicky designs, logos etc.

```html
<!DOCTYPE html>
<html lang="en">
<head>
<meta charset="utf-8">
<title>Verdalo Nutrition – Apple Cider Vinegar Gummy Label</title>
<link rel="stylesheet" href="https://fonts.googleapis.com/css2?family=Montserrat:wght@500;600;700;800&family=Roboto+Condensed:wght@400;700&family=Roboto:wght@400;500;700&family=Archivo+Black&display=swap">
<style>
:root{
  --red:#ec1f27;
  --red-soft:#f04a50;
  --red-deep:#8e0d12;
  --black:#0b0b0c;
  --panel:#161618;
  --white:#ffffff;
  --silver-1:#f2f2f2;
  --silver-2:#8a8a8a;
  --text-grey:#e6e6e6;
}
*{margin:0;padding:0;box-sizing:border-box}
html,body{width:1200px;height:983px;overflow:hidden;background:var(--white)}
body{position:relative;font-family:"Roboto Condensed",sans-serif}

.brand-heading{position:absolute;top:150px;left:0;width:1200px;text-align:center;color:var(--black)}
.brand-heading .name{font-family:"Montserrat",sans-serif;font-weight:600;font-size:46px;letter-spacing:1px;line-height:1}
.brand-heading .sub{font-family:"Montserrat",sans-serif;font-weight:600;font-size:30px;letter-spacing:3px;margin-top:6px}
.brand-heading .dot{display:inline-block;width:14px;height:14px;border-radius:50%;background:#2c9a3c;margin-left:8px;vertical-align:middle}

.label{position:absolute;left:20px;top:420px;width:1160px;height:290px;background:var(--black);overflow:hidden;box-shadow:0 2px 6px rgba(0,0,0,.25)}
.label .texture{position:absolute;inset:0;background:radial-gradient(circle at 50% 40%,#2a2a2c 0,#151516 45%,#0a0a0a 100%)}
.label .red-band{position:absolute;left:0;right:0;top:212px;height:78px;background:linear-gradient(180deg,var(--red-deep) 0,#b3151b 40%,#7a0a0e 100%)}
.label .red-band::before{content:"";position:absolute;left:0;right:0;top:-4px;height:4px;background:var(--red)}
.barcode-zone{position:absolute;left:0;top:0;width:60px;height:290px;background:var(--white)}
.barcode-zone span{position:absolute;left:30px;top:145px;transform:translate(-50%,-50%) rotate(90deg);white-space:nowrap;font-family:"Roboto",sans-serif;font-size:15px;color:#222}

.info{position:absolute;left:73px;top:22px;width:230px;color:var(--text-grey);font-size:9.2px;line-height:1.22}
.info p{margin-bottom:6px}
.info .lead{color:var(--red-soft)}
.info .keep{background:var(--red);color:var(--white);font-weight:700;font-size:10.5px;text-align:center;padding:5px 0;line-height:1.3;margin:4px 0 6px}
.info .allergen{font-size:7.8px;margin-left:3px}
.info .disclaimer{border:1px solid var(--red);padding:4px 7px;font-size:7.8px;line-height:1.3}
.mfg{position:absolute;left:73px;top:237px;width:230px;height:40px;border:1px solid var(--white);border-top:none}
.mfg::before,.mfg::after{content:"";position:absolute;top:0;height:1px;background:var(--white);width:55px}
.mfg::before{left:0}.mfg::after{right:0}
.mfg span{position:absolute;top:-6px;left:0;width:100%;text-align:center;color:var(--white);font-weight:700;font-size:10.5px}

.front{position:absolute;left:430px;top:0;width:340px;height:290px;text-align:center}
.front .logo{position:absolute;top:24px;left:0;width:100%;color:var(--white);font-family:"Montserrat",sans-serif;font-weight:600;line-height:1}
.front .logo .n1{font-size:18px;display:block}
.front .logo .n2{font-size:16px;letter-spacing:1px;display:block;margin-top:2px}
.front .logo .dot{display:inline-block;width:8px;height:8px;border-radius:50%;background:#2c9a3c;margin-left:4px;vertical-align:middle}
.title{position:absolute;left:0;width:100%;font-family:"Montserrat",sans-serif;font-weight:700;line-height:1;letter-spacing:1px}
.title.apple{top:82px;font-size:38px;color:var(--red)}
.title.vinegar,.title.gummy{font-size:39px;background:linear-gradient(180deg,var(--silver-1) 20%,var(--silver-2) 60%,#d8d8d8 90%);-webkit-background-clip:text;background-clip:text;color:transparent}
.title.vinegar{top:122px}
.title.gummy{top:160px}
.badges{position:absolute;top:222px;left:83px;display:flex;gap:12px}
.badge{width:33px;height:33px;border-radius:50%;border:2px solid var(--white);background:var(--red);color:var(--white);font-family:"Roboto",sans-serif;font-weight:700;font-size:6.5px;display:flex;align-items:flex-end;justify-content:center;padding-bottom:5px}
.badge svg{position:absolute;margin-bottom:10px}
.supplement-pill{position:absolute;top:263px;left:75px;width:148px;height:27px;background:var(--black);border-radius:8px 8px 0 0;color:var(--white);font-family:"Roboto",sans-serif;font-weight:700;font-style:italic;font-size:9.5px;letter-spacing:1.6px;line-height:27px}
.count{position:absolute;top:205px;left:238px;width:84px;height:84px;border-radius:50%;background:radial-gradient(circle at 40% 30%,#ffffff 0,#c9c9c9 45%,#777 100%);border:3px solid #2b2b2b;color:#111;font-family:"Montserrat",sans-serif;font-weight:800;line-height:1}
.count .num{font-size:26px;margin-top:16px;display:block}
.count .lbl{font-size:7.5px;display:block;margin-top:2px}

.facts{position:absolute;left:863px;top:24px;width:227px;height:248px;border:1.5px solid var(--white);padding:3px 6px;color:var(--white);font-family:"Roboto",sans-serif;font-size:8.4px}
.facts h2{font-family:"Archivo Black",sans-serif;font-weight:400;font-size:16.5px;text-align:center;line-height:1.1}
.facts .serving{font-weight:700;font-size:8.8px;line-height:1.35;border-bottom:4px solid var(--white);padding-bottom:3px}
.facts .head{text-align:right;font-weight:700;font-size:8px;padding:3px 0 2px;border-bottom:2px solid var(--white)}
.row{display:grid;grid-template-columns:1fr 52px 22px;border-bottom:.6px solid #bbb;line-height:11.6px}
.row .a,.row .d{text-align:right}
.row.i1 .n{padding-left:8px}.row.i2 .n{padding-left:14px}
.row:last-of-type{border-bottom:4px solid var(--white)}
.facts .notes{margin-top:4px;line-height:1.35;font-size:8.2px}
.other{position:absolute;left:1104px;top:16px;width:34px;height:258px}
.other p{position:absolute;left:17px;top:129px;width:258px;transform:translate(-50%,-50%) rotate(-90deg);color:var(--white);font-family:"Roboto",sans-serif;font-size:7.2px;line-height:1.25}
.other b{color:var(--red);font-weight:500}
</style>
</head>
<body>

<header class="brand-heading">
  <div class="name">Verdalo<span class="dot"></span></div>
  <div class="sub">NUTRITION</div>
</header>

<section class="label">
  <div class="texture"></div>
  <div class="red-band"></div>

  <div class="barcode-zone"><span>Bar-Code Zone</span></div>

  <div class="info">
    <p><span class="lead">Suggested Use:</span> Take one (1) gummy daily or as directed by a healthcare professional.</p>
    <p><span class="lead">Caution:</span> If you are pregnant, nursing, taking any medications or have any medical condition, consult your doctor before use. Discontinue use and consult your doctor if any adverse reactions occur.</p>
    <div class="keep">KEEP OUT OF REACH OF CHILDREN.<br>STORE AT ROOM TEMPERATURE.</div>
    <p class="allergen"><span class="lead">ALLERGEN WARNING:</span> This product contains tree nuts (coconut).</p>
    <div class="disclaimer">†These statements have not been evaluated by the QRB. This product is not intended to diagnose, cure, treat or prevent any disease.</div>
  </div>
  <div class="mfg"><span>MANUFACTURED FOR:</span></div>

  <div class="front">
    <div class="logo"><span class="n1">Verdalo<span class="dot"></span></span><span class="n2">NUTRITION</span></div>
    <div class="title apple">APPLE CIDER</div>
    <div class="title vinegar">VINEGAR</div>
    <div class="title gummy">GUMMY</div>
    <div class="badges">
      <div class="badge">Vegan</div>
      <div class="badge">GMO FREE</div>
      <div class="badge">GLUTEN</div>
    </div>
    <div class="supplement-pill">DIETARY SUPPLEMENT</div>
    <div class="count"><span class="num">60</span><span class="lbl">GUMMIES</span><span class="lbl">NATURAL</span></div>
  </div>

  <div class="facts">
    <h2>Supplement Facts</h2>
    <div class="serving">Serving Size:&nbsp; 1 Gummy<br>Servings Per Container: 60</div>
    <div class="head">Amount Per Serving&nbsp; % DV</div>
    <div class="row"><span class="n">Calories</span><span class="a">10</span><span class="d"></span></div>
    <div class="row"><span class="n">Total Carbohydrates</span><span class="a">3 g</span><span class="d">&lt;1%</span></div>
    <div class="row i1"><span class="n">Total Sugars</span><span class="a">2 g</span><span class="d">**</span></div>
    <div class="row i2"><span class="n">Includes 2 g Added Sugars</span><span class="a"></span><span class="d">4%</span></div>
    <div class="row"><span class="n">Vitamin B-6 (as Pyridoxine HCl)</span><span class="a">0.5 mg</span><span class="d">29%</span></div>
    <div class="row"><span class="n">Folate (120 mcg Folic Acid)</span><span class="a">200 mcg DFE</span><span class="d">50%</span></div>
    <div class="row"><span class="n">Vitamin B-12 (as Cyanocobalamin)</span><span class="a">1.2 mcg</span><span class="d">50%</span></div>
    <div class="row"><span class="n">Iodine (as Potassium Iodide)</span><span class="a">50 mcg</span><span class="d">33%</span></div>
    <div class="row"><span class="n">Apple Cider Vinegar Powder (fruit)<br>(providing 5% total acid)</span><span class="a">500 mg</span><span class="d">**</span></div>
    <div class="row"><span class="n">Pomegranate Juice Powder</span><span class="a">40 mcg</span><span class="d">**</span></div>
    <div class="row"><span class="n">Beet Root Juice Powder</span><span class="a">40 mcg</span><span class="d">**</span></div>
    <div class="notes">* % Daily Value Based on 2,000 Calorie Diet<br>** Daily Value Not Established</div>
  </div>

  <div class="other"><p><b>Other Ingredients:</b> Glucose Syrup, Sugar, Glucose, Pectin, Sodium Citrate, Citric Acid, Natural Apple Flavor, Vegetable Oil, Liquid Apple Cider Vinegar, Purple carrot Juice Concentrate and Beta Carotene.</p></div>
</section>

</body>
</html>
```